Raw Material for Personal Care Products

We need to make a brochure with the products we sell to manufacture natural personal care products

Target Market(s)

Cosmetics Manufacturers

Industry/Entity Type

Cosmetics

Colors
00AB8E
00BBA5
67D7C9
C6EFE9
E9F9F6

Requirements
Must have
• Images associated with nature, organics
Should not have
• Chemicals industries, refinaries

```html
<!DOCTYPE html>
<html lang="es">
<head>
<meta charset="utf-8">
<title>Materias Primas Naturales Orgánicas para Cuidado Personal</title>
<link rel="stylesheet" href="https://fonts.googleapis.com/css2?family=Jost:wght@300;400;600;700&display=swap">
<style>
  :root {
    --green-dark: #2c7f3b;
    --green-text: #2f8240;
    --green-soft: #c4df9b;
    --green-frame: #c9e4a3;
    --white: #ffffff;
    --scene-light: #efefef;
    --scene-mid: #d9d9d9;
    --photo-a: #8f8f8f;
    --photo-b: #dcdad6;
  }
  * { margin: 0; padding: 0; box-sizing: border-box; }
  html, body { width: 927px; height: 1200px; overflow: hidden; background: var(--white); }
  body { font-family: "Jost", sans-serif; color: var(--green-text); }
  .brochure { position: relative; width: 927px; height: 1200px; overflow: hidden; background: var(--white); }
  .abs { position: absolute; }

  .title {
    left: 63px; top: 50px; font-size: 29.5px; line-height: 36px;
    font-weight: 700; color: var(--green-dark);
  }
  .brand {
    left: 760px; top: 70px; width: 130px; display: flex; flex-direction: column; align-items: center; gap: 6px;
  }
  .brand-mark { width: 22px; height: 22px; background: var(--green-soft); }
  .brand-name { font-size: 15px; font-weight: 600; color: var(--green-dark); letter-spacing: 1px; text-align: center; line-height: 17px; }

  .scene-band {
    left: 0; top: 153px; width: 927px; height: 912px;
    background: linear-gradient(160deg, var(--scene-light) 0%, #f6f6f6 45%, var(--scene-mid) 100%);
  }
  .photo-frame { left: 491px; top: 175px; width: 403px; height: 534px; background: var(--green-frame); }
  .photo {
    left: 500px; top: 185px; width: 384px; height: 512px;
    background: linear-gradient(120deg, var(--photo-a) 0%, #b9b7b3 45%, var(--photo-b) 100%);
  }

  .panel { left: 0; width: 575px; background: var(--green-soft); }
  .panel-oils { top: 224px; height: 358px; }
  .panel-surf { top: 651px; height: 380px; }
  .label-white { background: var(--white); display: flex; align-items: center; }
  .label-oils { left: 33px; top: 182px; width: 388px; height: 71px; padding-left: 31px; }
  .label-surf { left: 33px; top: 608px; width: 331px; height: 71px; padding-left: 34px; }
  .section-title { font-size: 22px; font-weight: 700; color: var(--green-dark); }

  .list { list-style: none; font-size: 17px; font-weight: 300; line-height: 18.2px; color: var(--green-text); }
  .list-col1 { left: 67px; top: 277px; }
  .list-col2 { left: 309px; top: 277px; }
  .note { left: 33px; top: 540px; font-size: 17px; font-weight: 300; }

  .subhead { font-size: 17px; font-weight: 600; color: var(--green-dark); }
  .sub-amino { left: 67px; top: 701px; }
  .list-amino { left: 67px; top: 727px; }
  .sub-alkyl { left: 67px; top: 854px; }
  .list-alkyl { left: 67px; top: 879px; }

  .box-white { background: var(--white); }
  .box-frag { left: 590px; top: 723px; width: 337px; height: 104px; }
  .box-cert { left: 590px; top: 891px; width: 337px; height: 140px; }
  .label-green { background: var(--green-soft); display: flex; align-items: center; justify-content: center;
    font-size: 21px; font-weight: 700; color: var(--green-dark); letter-spacing: 0.3px; }
  .label-frag { left: 657px; top: 680px; width: 202px; height: 70px; }
  .label-cert { left: 634px; top: 848px; width: 249px; height: 72px; }
  .center-list { list-style: none; text-align: center; font-size: 14.5px; font-weight: 300; line-height: 18.2px; }
  .frag-list { left: 590px; top: 768px; width: 337px; }
  .cert-list { left: 600px; top: 939px; width: 337px; }

  .contact-label { left: 67px; top: 1091px; font-size: 20px; font-weight: 400; color: var(--green-dark); }
  .contact-phone { left: 67px; top: 1130px; font-size: 21px; font-weight: 700; color: var(--green-dark); letter-spacing: 0.5px; }
  .contact-address { left: 697px; top: 1128px; font-size: 19px; font-weight: 400; color: var(--green-dark); }
</style>
</head>
<body>
<main class="brochure">
  <h1 class="abs title">Materias Primas Naturales Orgánicas<br>para Cuidado Personal</h1>

  <div class="abs brand">
    <span class="brand-mark"></span>
    <span class="brand-name">VERDANA QUIMICA</span>
  </div>

  <div class="abs scene-band" role="img" aria-label="Fondo de tela blanca suave con hojas verdes de planta"></div>
  <div class="abs photo-frame"></div>
  <div class="abs photo" role="img" aria-label="Mano con hojas de menta sobre la piel ante una pared iluminada"></div>

  <section>
    <div class="abs panel panel-oils"></div>
    <div class="abs label-white label-oils"><h2 class="section-title">Aceites y Mantecas Naturales</h2></div>
    <ul class="abs list list-col1">
      <li>Aceite de Acaí</li><li>Aceite de Aguacate</li><li>Aceite de Almendra Dulce</li>
      <li>Aceite de Andiroba</li><li>Aceite de Argán</li><li>Aceite de Avellana</li>
      <li>Aceite de Babacu</li><li>Aceite de Buriti</li><li>Aceite de Castor</li>
      <li>Aceite de Coco</li><li>Aceite de de Nuez</li><li>Aceite de Girasol</li><li>Aceite de Jojoba</li>
    </ul>
    <ul class="abs list list-col2">
      <li>Aceite de Macadamia</li><li>Aceite de Oliva</li><li>Aceite de Pracaxi</li>
      <li>Aceite de Semilla de Durazno</li><li>Aceite de Semilla de Uva</li><li>Aceite de Sesamo</li>
      <li>Aceite de Soya</li><li>Aceite de Zanahoria</li><li>Manteca de Cupuacu</li>
      <li>Manteca de Karite</li><li>Manteca de Murumuru</li><li>Manteca de Ucuba</li><li>Scrub de Murumuru</li>
    </ul>
    <p class="abs note">Los Aceites están disponibles Vírgenes, Refinados, desodorizados,</p>
  </section>

  <section>
    <div class="abs panel panel-surf"></div>
    <div class="abs label-white label-surf"><h2 class="section-title">Surfactantes Naturales</h2></div>
    <h3 class="abs subhead sub-amino">Surfactante Amino Acido</h3>
    <ul class="abs list list-amino">
      <li>Glicinato de Potasio Cocoil y Glicerina</li><li>Glicinato de Potasio Cocoil</li>
      <li>Glicinato de Sodio Cocoil y Glicerina</li><li>Glicinato de Sodio Cocoil</li><li>Glutamato de Sodio Cocoil</li>
    </ul>
    <h3 class="abs subhead sub-alkyl">Sufactante Alquil Glucosido</h3>
    <ul class="abs list list-alkyl">
      <li>Glucosido Laurico</li><li>Glucosido de Coco</li><li>Glucosido Decilico</li>
      <li>Hidroxipropil Sulfonato Laurilglucosido de Sodio</li>
      <li>Carboxilato Glucosa Laurico de Sodio y Glucosido Laurico</li>
      <li>Cocoil Isetianato de Sodio (SCI)</li><li>CocoamidoPropilBetaine (CAPB)</li>
    </ul>
  </section>

  <section>
    <div class="abs box-white box-frag"></div>
    <h2 class="abs label-green label-frag">FRAGANCIAS</h2>
    <ul class="abs center-list frag-list">
      <li>Fragancias Convencionales</li><li>Fragancias Naturales 100% (FLORNAT)</li>
    </ul>
  </section>

  <section>
    <div class="abs box-white box-cert"></div>
    <h2 class="abs label-green label-cert">CERTIFICACIONES</h2>
    <ul class="abs center-list cert-list">
      <li>Ecoverde (Organic Farming Product)</li><li>Cosmara Organic</li>
      <li>Kosher (Unión Kashrut)</li><li>Agro Organic</li>
    </ul>
  </section>

  <footer>
    <p class="abs contact-label">Contact Us</p>
    <p class="abs contact-phone">123–456–789</p>
    <p class="abs contact-address">Anywhere St. City</p>
  </footer>
</main>
</body>
</html>
```